Digital billboard sales for the nema region

Business card that is informative and unique. Whether the card can be applicable to a real world application or it is 3D or if something changed on the card. I want it to be an eye catcher

Went on vacation/holiday

```html
<!DOCTYPE html>
<html lang="en">
<head>
<meta charset="utf-8">
<title>Business Card – Front and Back</title>
<link rel="stylesheet" href="https://fonts.googleapis.com/css2?family=Oswald:wght@500&family=Raleway:wght@600&family=Roboto:ital,wght@1,900&display=swap">
<style>
  :root {
    --page-bg: #eef1f4;
    --brand-blue: #2f80c9;
    --brand-blue-deep: #1f6db8;
    --brand-blue-light: #4e97d6;
    --pill-blue: #2ea4e2;
    --band-white: #ffffff;
    --name-blue: #1d63b0;
    --muted-grey: #9aa4ad;
    --soft-text: #bfe3fb;
    --text-white: #ffffff;
  }
  * { margin: 0; padding: 0; box-sizing: border-box; }
  html, body {
    width: 1200px; height: 900px; overflow: hidden;
    background: var(--page-bg);
  }
  .canvas { position: relative; width: 1200px; height: 900px; }
  .card {
    position: absolute; left: 285px; width: 630px; height: 360px;
    overflow: hidden; border-radius: 4px;
    box-shadow: 0 10px 28px rgba(20, 50, 90, 0.22);
  }
  .card--front {
    top: 50px;
    background:
      linear-gradient(125deg, rgba(255,255,255,0) 55%, rgba(255,255,255,0.10) 55.2%, rgba(255,255,255,0.02) 80%),
      linear-gradient(160deg, var(--brand-blue-light), var(--brand-blue));
  }
  .brand {
    position: absolute; left: 0; right: 0; top: 120px;
    display: flex; flex-direction: column; align-items: center; gap: 16px;
  }
  .brand__dot {
    width: 64px; height: 64px; border-radius: 50%;
    background: var(--soft-text);
  }
  .brand__name {
    font-family: "Oswald", sans-serif; font-weight: 500;
    font-size: 36px; letter-spacing: 0.5px; color: var(--soft-text);
  }

  .card--back { top: 490px; background: var(--brand-blue); }
  .card__panel {
    position: absolute; left: 340px; top: 44px; right: 0; bottom: 0;
    background: var(--brand-blue-deep);
  }
  .card__circle {
    position: absolute; left: 400px; top: 110px;
    width: 240px; height: 240px; border-radius: 50%;
    background: var(--brand-blue-light); opacity: 0.55;
  }
  .name-band {
    position: absolute; left: 0; top: 22px; width: 420px; height: 52px;
    background: var(--band-white);
    clip-path: polygon(0 0, 100% 0, 94% 100%, 0 100%);
    display: flex; align-items: center; padding-left: 22px; gap: 10px;
  }
  .name-band__stripe {
    position: absolute; left: 420px; top: 22px; right: 0; height: 8px;
    background: var(--band-white);
  }
  .person-name {
    font-family: "Roboto", sans-serif; font-style: italic; font-weight: 900;
    font-size: 32px; color: var(--name-blue);
  }
  .person-role {
    font-family: "Raleway", sans-serif; font-weight: 600;
    font-size: 14px; color: var(--muted-grey); margin-top: 8px;
  }
  .contact-list {
    position: absolute; left: 18px; top: 96px; list-style: none;
    display: flex; flex-direction: column; gap: 12px;
  }
  .contact-item {
    height: 48px; width: 350px; border-radius: 24px;
    background: var(--pill-blue);
    display: flex; align-items: center; gap: 16px; padding-left: 16px;
    font-family: "Raleway", sans-serif; font-weight: 600;
    font-size: 16px; color: var(--text-white); white-space: nowrap;
  }
  .contact-item--wide { width: 380px; }
  .contact-item svg { width: 22px; height: 22px; flex: none; fill: var(--text-white); }
</style>
</head>
<body>
<main class="canvas">

  <section class="card card--front" aria-label="Card front">
    <div class="brand">
      <span class="brand__dot"></span>
      <span class="brand__name">Brightpost Media</span>
    </div>
  </section>

  <section class="card card--back" aria-label="Card back">
    <div class="card__panel"></div>
    <div class="card__circle"></div>
    <div class="name-band__stripe"></div>
    <div class="name-band">
      <span class="person-name">Lena Marsh</span>
      <span class="person-role">CEO</span>
    </div>
    <ul class="contact-list">
      <li class="contact-item">
        <svg viewBox="0 0 24 24" aria-hidden="true"><path d="M12 2a7 7 0 0 0-7 7c0 5 7 13 7 13s7-8 7-13a7 7 0 0 0-7-7zm0 9.5a2.5 2.5 0 1 1 0-5 2.5 2.5 0 0 1 0 5z"/></svg>
        14 Harbor Lane, Dubai, UAE
      </li>
      <li class="contact-item">
        <svg viewBox="0 0 24 24" aria-hidden="true"><path d="M6.6 10.8a15 15 0 0 0 6.6 6.6l2.2-2.2a1 1 0 0 1 1-.25 11.4 11.4 0 0 0 3.6.57 1 1 0 0 1 1 1V20a1 1 0 0 1-1 1A17 17 0 0 1 3 4a1 1 0 0 1 1-1h3.5a1 1 0 0 1 1 1c0 1.25.2 2.45.57 3.57a1 1 0 0 1-.25 1z"/></svg>
        (971) 555 0142
      </li>
      <li class="contact-item">
        <svg viewBox="0 0 24 24" aria-hidden="true"><path d="M3 5h18a1 1 0 0 1 1 1v.4l-10 6.2L2 6.4V6a1 1 0 0 1 1-1zm-1 3.7 10 6.2 10-6.2V18a1 1 0 0 1-1 1H3a1 1 0 0 1-1-1z"/></svg>
        lena@brightpost.io
      </li>
      <li class="contact-item contact-item--wide">
        <svg viewBox="0 0 24 24" aria-hidden="true"><path d="M12 2a10 10 0 1 0 0 20 10 10 0 0 0 0-20zm-1 17.9A8 8 0 0 1 4 12l5 5v1a2 2 0 0 0 2 2zm6.9-2.5A2 2 0 0 0 16 16h-1v-3a1 1 0 0 0-1-1H8v-2h2a1 1 0 0 0 1-1V7h2a2 2 0 0 0 2-2v-.4a8 8 0 0 1 2.9 12.8z"/></svg>
        www.brightpost.io
      </li>
    </ul>
  </section>

</main>
</body>
</html>
```